R&T Cleanwave Stripping Business Card

We are in need of a business card design for our new Texas based company called 'R&T Cleanwave Stripping'. Our new innovative mobile media blasting service utilizes recycled material and a new water based process that eliminates all dust (i.e. as apposed to the old sand blasting format). Our 'advanced surface preparation' service targets multiple industries such as automotive, Industrial, marine and structural (graffiti removal). We would like to see the design include a recycling type logo or concept that utilizes colors such as black, various shades of green, some white, yellow and/or grey (e.g. perhaps a blackish background). The final design should look simple and professional and should clearly communicate the environmentally friendly approach through logo or design (i.e. Eco-Friendly, Go Green or Blast Green methodologies). Thank you in advance!
Updates

Please pardon any inconvenience. We have decided to pursue a two sided business card. All original information/designs requirements remains the same for the front. However, we would like back of the card to state the following: "We bring the power of Hydroveil Media Scouring equipment to your location. We can remove any coating from any surface. Bullets include: Paint Stripping, Auto Restoration, Graffiti Removal, Black Walls & Stone, Concrete, Boats, Iron Fences, Tractors & Trailers, Pools & Fountains, Wood Restoration.

Industry/Entity Type

Recycling

Contact Information for Business Card

R&T Cleanwave Stripping, LLC - Gordon Pelly, MBA, PMP - cell: 915-382-6091, office: 915-627-8853 - gpelly@rtcleanwavestripping.com - CEO/Founder

Requirements
Must have
• Recycle or environmentally friendly logos or design.
Nice to have
• Business oriented design with an aggressive look. Also, if possible would like to see R&T incorporated into the design or logo. Please note that we have decided to add the option of adding details to the back of the card (2 sided). The front should contain the logo/design and the back should have the following details listed: "We bring the power of Hydroveil Media Scouring equipment to your location. We can remove any coating from any surface. Bullets include: Paint Stripping, Auto Restoration, Graffiti Removal, Black Walls & Stone, Concrete, Boats, Iron Fences, Tractors & Trailers, Pools & Fountains, Wood Restoration.

```html
<!DOCTYPE html>
<html lang="en">
<head>
<meta charset="utf-8">
<title>R&amp;T Cleanwave Stripping — Business Card</title>
<link href="https://fonts.googleapis.com/css2?family=Open+Sans:wght@400;600&family=Russo+One&family=Roboto+Condensed:wght@400&display=swap" rel="stylesheet">
<style>
  :root {
    --page-bg: #efeae2;
    --green-deep: #0b3519;
    --green-mid: #1a6a33;
    --green-bright: #3aa543;
    --green-band: #1f8a3a;
    --leaf-tone: #245f30;
    --yellow: #f2e21a;
    --grey-light: #eeeeee;
    --grey-mid: #c9c9c9;
    --ink: #333333;
    --ink-soft: #4a4a4a;
    --red: #d6232a;
    --white: #ffffff;
  }
  html, body {
    margin: 0;
    padding: 0;
    width: 1200px;
    height: 913px;
    overflow: hidden;
    background: var(--page-bg);
  }
  .canvas {
    position: relative;
    width: 1200px;
    height: 913px;
  }
  .card {
    position: absolute;
    top: 300px;
    width: 530px;
    height: 310px;
    overflow: hidden;
    box-shadow: 0 10px 28px rgba(0,0,0,0.25);
  }
  /* Front */
  .card-front {
    left: 40px;
    background: linear-gradient(135deg, var(--green-deep) 0%, var(--green-mid) 100%);
  }
  .front-leaf-decor {
    position: absolute;
    top: 0;
    right: 0;
    width: 90px;
    height: 190px;
    background: linear-gradient(180deg, rgba(36,95,48,0.9), rgba(36,95,48,0.2));
  }
  .holder {
    position: absolute;
    left: 28px;
    top: 30px;
    color: var(--white);
    font-family: "Open Sans", sans-serif;
  }
  .holder-name { font-size: 19px; font-weight: 600; }
  .holder-title { font-size: 13px; margin-top: 2px; }
  .front-mark {
    position: absolute;
    left: 0;
    right: 0;
    top: 70px;
    text-align: center;
  }
  .mark-circle {
    display: inline-block;
    width: 56px;
    height: 56px;
    border-radius: 50%;
    border: 4px solid var(--green-bright);
    box-sizing: border-box;
  }
  .front-company {
    margin-top: 8px;
    font-family: "Russo One", sans-serif;
    font-size: 23px;
    color: var(--yellow);
    letter-spacing: 0.5px;
  }
  .front-contact-band {
    position: absolute;
    left: 0;
    bottom: 0;
    width: 530px;
    height: 110px;
  }
  .contact-lines {
    position: absolute;
    left: 28px;
    bottom: 20px;
    font-family: "Open Sans", sans-serif;
    font-size: 16px;
    color: var(--ink-soft);
    line-height: 1.55;
  }
  .contact-line { display: flex; align-items: center; gap: 8px; }
  .contact-line svg { flex: none; }
  /* Back */
  .card-back {
    left: 630px;
    background: linear-gradient(180deg, var(--white), var(--grey-light));
  }
  .back-band-top, .back-band-bottom {
    position: absolute;
    left: 0;
    width: 100%;
    background: linear-gradient(90deg, var(--green-mid), var(--green-bright), var(--green-mid));
  }
  .back-band-top { top: 0; height: 9px; }
  .back-band-bottom { bottom: 0; height: 14px; }
  .back-mark {
    position: absolute;
    left: 22px;
    top: 22px;
    display: flex;
    align-items: center;
    gap: 12px;
  }
  .back-mark .mark-circle { width: 46px; height: 46px; border-width: 3px; }
  .back-company {
    font-family: "Russo One", sans-serif;
    font-size: 21px;
    color: var(--red);
  }
  .back-copy {
    position: absolute;
    left: 20px;
    right: 20px;
    top: 90px;
    text-align: center;
    font-family: "Roboto Condensed", sans-serif;
    color: var(--ink);
  }
  .back-lead { font-size: 17px; line-height: 1.35; margin: 0; }
  .back-claim { font-size: 17px; color: var(--red); margin: 6px 0 4px; }
  .service-list { font-size: 15px; line-height: 1.45; margin: 0; }
  .dot { color: var(--red); }
</style>
</head>
<body>
<div class="canvas">

  <section class="card card-front" aria-label="Card front">
    <div class="front-leaf-decor" role="img" aria-label="Decorative green leaves"></div>
    <div class="holder">
      <div class="holder-name">Gordon Pelly</div>
      <div class="holder-title">MBA, PMP</div>
    </div>
    <div class="front-mark">
      <span class="mark-circle"></span>
      <div class="front-company">R&amp;T CLEANWAVE STRIPPING, LLC</div>
    </div>
    <svg class="front-contact-band" viewBox="0 0 530 110" aria-hidden="true">
      <defs>
        <linearGradient id="greyBand" x1="0" y1="0" x2="0" y2="1">
          <stop offset="0" stop-color="#f4f4f4"/>
          <stop offset="1" stop-color="#bdbdbd"/>
        </linearGradient>
      </defs>
      <path d="M0 18 Q265 -4 530 0 L530 110 L0 110 Z" fill="#3aa543"/>
      <path d="M0 24 Q265 4 530 7 L530 110 L0 110 Z" fill="url(#greyBand)"/>
    </svg>
    <div class="contact-lines">
      <div class="contact-line">
        <svg width="16" height="16" viewBox="0 0 16 16" aria-hidden="true"><rect x="0.5" y="0.5" width="15" height="15" rx="2" fill="#3aa543"/><path d="M5 3.5 L7 5.5 L6 7 Q7 9 9 10 L10.5 9 L12.5 11 L11 12.5 Q6 12 3.5 5 Z" fill="#fff"/></svg>
        <span>915-382-6091, office: 915-627-8853</span>
      </div>
      <div class="contact-line">
        <svg width="16" height="16" viewBox="0 0 16 16" aria-hidden="true"><rect x="0.5" y="0.5" width="15" height="15" rx="2" fill="#3aa543"/><rect x="3" y="4.5" width="10" height="7" fill="none" stroke="#fff" stroke-width="1.2"/><path d="M3 4.5 L8 8.5 L13 4.5" fill="none" stroke="#fff" stroke-width="1.2"/></svg>
        <span>gpelly@rtcleanwavestripping.com</span>
      </div>
    </div>
  </section>

  <section class="card card-back" aria-label="Card back">
    <div class="back-band-top"></div>
    <div class="back-mark">
      <span class="mark-circle"></span>
      <span class="back-company">R&amp;T CLEANWAVE STRIPPING, LLC</span>
    </div>
    <div class="back-copy">
      <p class="back-lead">We bring the power of Hydroveil Media Scouring<br>equipment to your location.</p>
      <p class="back-claim">We can remove any coating from any surface.</p>
      <p class="service-list">
        <span class="dot">•</span> Paint Stripping <span class="dot">•</span> Auto Restoration <span class="dot">•</span> Graffiti Removal<br>
        Black Walls &amp; Stone, Concrete, Boats <span class="dot">•</span> Iron Fences<br>
        Tractors &amp; Trailers <span class="dot">•</span> Pools &amp; Fountains,<br>
        <span class="dot">•</span> Wood Restoration.
      </p>
    </div>
    <div class="back-band-bottom"></div>
  </section>

</div>
</body>
</html>
```